Guaranteed Job - Sleek Sexy Business Card UV Spot

Im looking for a sleek and sexy business card, that resembles elite or VIP status status.
our business is corinvale.example
you can view our products on there, but our main audience for handing out our cards will be for people in the hospitality industry, so it will need to impress high management and CEO of hotels and restaurants, bars, clubs etc...
the card features will have UV spot on both sides, 400gsm stock. standard size.
Artwork should be 86 x 54mm + 2mm bleed = 90 x 58mm
it should have a nice "unique" uv spot pattern that highlights the card, not a repeated pattern, theres no originality there, and it will be disregarded.
The written material will be:
Corin Vale Hospitality College (logo)
Tobin Marsh
Director
Phone: 1300 615 737
Mobile: 0455 817 296
Email: info@corinvale.example
website: www.corinvale.example
I'm looking for originality here, i don't want just a simple stock card, want something that has a wow factor for people.
You will find the logo attached. you may invert the white to black words to suit the background as you please.
thank you and good luck
As a side note, ive received a lot of proposals, im too busy to give feedback to each and every one, so if i havent provided feedback for your design within 24 hours, then consider it not acceptable, and you could resubmit another design.
So far i have not seen any design that stood out for me, they all seem pretty generic. there nothing thats unique, i would figure for the amount that im offering, that people would put some more effort and creativity into the design.
so far over 200 designs submitted, and nothing i have seen looks very original, everything looks like a different variation of the same stuff, i said it very clearly i wanted something unique, the only thing that has come close to it so far is this one
Reason: Ive received alot of design concepts and i have reviewed everyone, but i havent had time to give feedback to every single one, only the ones that have interested me, if i havent responded, its because i havent found it good enough.
so far only a few design have been on par with what ive been looking for, an attractive eye popping design.
heres a few of them,
http://files.pixelbazaar.example/design_img/51736/62418/62418_2840915_51736_image.jpg
http://files.pixelbazaar.example/design_img/51736/68254/68254_2841377_51736_image.jpg
theyre, both unique and original, and eye catching, the only thing theyre missing is the sexyness.
if you still think you have some creativity left in your minds, then throw it on here.
Reason: Sorry guys for the delay, I was in a serious accident and out of commission for the past few months, I'm just slowly recovering now, please bare with me as i try to attend to this project, it may take me awhile as I have other projects that are on standby, I'm not 100% at the moment, so im extending the deadline for 2 weeks right now. Thanks for your patience.
Hospitality

```html
<!DOCTYPE html>
<html lang="en">
<head>
<meta charset="utf-8">
<title>Corin Vale Hospitality College – Business Card</title>
<link rel="stylesheet" href="https://fonts.googleapis.com/css2?family=Open+Sans:wght@700&family=Great+Vibes&family=Tinos:wght@700&display=swap">
<style>
  :root {
    --ink: #000000;
    --white: #ffffff;
    --gold-bright: #f3d97a;
    --gold: #c9a53a;
    --gold-deep: #7a5a14;
    --bronze: #3a2a10;
    --bronze-dark: #120c04;
    --silver: #b9bcc2;
    --silver-dark: #6d7077;
  }
  * { margin: 0; padding: 0; box-sizing: border-box; }
  html, body {
    width: 1200px;
    height: 762px;
    overflow: hidden;
    background: var(--ink);
  }
  .card {
    position: relative;
    width: 1200px;
    height: 762px;
    background: var(--ink);
    overflow: hidden;
  }
  .hero-art {
    position: absolute;
    left: 0;
    top: 0;
    width: 540px;
    height: 515px;
    background:
      radial-gradient(ellipse 220px 90px at 170px 110px, rgba(220,224,230,0.55), rgba(120,124,130,0.25) 60%, transparent 100%),
      radial-gradient(ellipse 90px 230px at 420px 370px, rgba(243,217,122,0.45), rgba(201,165,58,0.15) 60%, transparent 100%),
      var(--ink);
  }
  .brand {
    position: absolute;
    left: 600px;
    top: 52px;
    width: 520px;
    text-align: center;
    color: var(--white);
    font-family: "Open Sans", sans-serif;
    font-weight: 700;
    line-height: 1.1;
  }
  .brand .brand-name { display: block; font-size: 56px; letter-spacing: 0.5px; }
  .brand .brand-sub { display: block; font-size: 34px; margin-top: 6px; }
  .holder-name {
    position: absolute;
    left: 26px;
    top: 418px;
    font-family: "Great Vibes", cursive;
    font-size: 62px;
    color: var(--white);
    white-space: nowrap;
  }
  .holder-title {
    position: absolute;
    left: 548px;
    top: 424px;
    font-family: "Open Sans", sans-serif;
    font-weight: 700;
    font-size: 56px;
    color: var(--white);
    line-height: 1;
  }
  .band {
    position: absolute;
    left: 0;
    width: 1200px;
  }
  .band-gold-top {
    top: 512px;
    height: 13px;
    background: linear-gradient(90deg, var(--gold-deep), var(--gold-bright) 40%, var(--gold) 70%, var(--bronze) 100%);
  }
  .band-gold-thin {
    top: 536px;
    height: 6px;
    background: linear-gradient(90deg, var(--gold-deep), var(--gold) 50%, var(--gold-bright));
  }
  .contact-panel {
    top: 545px;
    height: 184px;
    background:
      radial-gradient(ellipse 420px 70px at 280px 60px, rgba(122,90,20,0.55), transparent 100%),
      radial-gradient(ellipse 380px 60px at 900px 140px, rgba(122,90,20,0.45), transparent 100%),
      linear-gradient(180deg, var(--bronze), var(--bronze-dark) 50%, var(--bronze));
  }
  .band-gold-lower {
    top: 729px;
    height: 7px;
    background: linear-gradient(90deg, var(--gold-deep), var(--gold-bright) 50%, var(--gold));
  }
  .band-gold-bottom {
    top: 748px;
    height: 14px;
    background: linear-gradient(90deg, var(--gold-deep), var(--gold-bright) 45%, var(--gold) 80%, var(--gold-deep));
  }
  .contact-list {
    position: absolute;
    left: 300px;
    top: 562px;
    width: 600px;
    list-style: none;
    text-align: center;
    font-family: "Tinos", serif;
    font-weight: 700;
    font-size: 23px;
    line-height: 30px;
    color: var(--white);
  }
  .monogram {
    position: absolute;
    left: 994px;
    top: 660px;
    font-family: "Open Sans", sans-serif;
    font-weight: 700;
    font-size: 48px;
    letter-spacing: 2px;
    color: var(--silver);
    line-height: 1;
  }
</style>
</head>
<body>
  <div class="card">
    <div class="hero-art" role="img" aria-label="Chrome cocktail shaker tipping out a stream of golden sparkles"></div>

    <div class="brand">
      <span class="brand-name">Corin Vale</span>
      <span class="brand-sub">Hospitality College</span>
    </div>

    <div class="holder-name">Tobin Marsh</div>
    <div class="holder-title">Director</div>

    <div class="band band-gold-top"></div>
    <div class="band band-gold-thin"></div>
    <div class="band contact-panel" role="img" aria-label="Dark bronze marbled backdrop"></div>
    <div class="band band-gold-lower"></div>
    <div class="band band-gold-bottom"></div>

    <ul class="contact-list">
      <li>Telephone: 1300 615 737</li>
      <li>Mobile: 0455 817 296</li>
      <li>Email: info@corinvale.example</li>
      <li>Website: www.corinvale.example</li>
    </ul>

    <div class="monogram">CVHC</div>
  </div>
</body>
</html>
```